依頼詳細
デザインをお願いする当サイトのトップページの役割は、
・当該部門の抽象的イメージの表現
・各種コンテンツ(製品情報、ブログ記事)のポータル的機能
の2つを主軸に据えようと考えています。

デザインの条件として、
・サイトロゴはこちから指定したものを使用する。
・レスポンシブデザインを適用する。
とさせて頂きます。ついては、

開発したアプリ、サービス等の周知、蓄積した技術情報等の発信を行うためにWebサイトとして見栄えがする、
・ページ全体、および個々の要素の配色
・ボーダー、シャドウのデザイン
・各要素の質感
のデザインをご提案頂きたいです。

現在、こちらで添付のようなページレイアウトを検討していますが、あくまで案ですので、レイアウトも含めたデザインをご提案いただいても構いません。
ページ数
1ページ
希望イメージ
シンプル 複雑
単色 カラフル
暗い 明るい
日常 高級
遊び心 厳粛
未来的 伝統的
女性的 男性的
希望する色
ロゴのカラーバリエーションのいずれかにマッチする配色でお願いします。
納品ファイル
• 高解像度JPG (.jpg)
• イラストレーター形式 (.ai)
• フォトショップ形式 (.psd)
• PNG形式 (.png)
補足説明
ロゴには、カラーバリエーションがありますので、サイト全体の配色に合うものを
適宜選択していただければと思います。
〆切を延長させて頂きます。

シンプルでわかりやすいデザインがサイトにマッチすると思いました。

たくさんのご提案をありがとうございます。
今後ともよろしくお願いします。

```html
<!DOCTYPE html>
<html lang="ja">
<head>
<meta charset="utf-8">
<title>Norte Studio</title>
<link rel="stylesheet" href="https://fonts.googleapis.com/css2?family=Lato:wght@300;400;700&family=Noto+Sans+JP:wght@300;400;500&display=swap">
<style>
:root{
  --ink:#333;
  --muted:#777;
  --line:#d8d8d8;
  --paper:#fff;
  --accent:#b6cc1c;
  --accent-dark:#98ab12;
  --red:#e0283c;
  --footer:#2e2e2e;
  --footer-text:#bbb;
}
*{box-sizing:border-box;margin:0;padding:0}
html,body{width:1200px;height:2428px;overflow:hidden;background:var(--paper)}
body{font-family:"Noto Sans JP","Lato",sans-serif;color:var(--ink);position:relative}
.abs{position:absolute}

/* header */
.site-header{left:0;top:0;width:1200px;height:80px;background:var(--paper);border-bottom:1px solid var(--line)}
.brand{left:120px;top:24px;font-family:"Lato",sans-serif;font-weight:700;font-size:24px;color:var(--ink);letter-spacing:1px}
.main-nav{right:110px;top:0;height:80px;display:flex;align-items:center}
.main-nav a{font-family:"Lato",sans-serif;font-size:15px;letter-spacing:1.5px;color:var(--ink);text-decoration:none;padding:0 32px;border-left:1px solid var(--line)}
.main-nav a:last-child{border-right:1px solid var(--line)}

/* hero */
.hero{left:0;top:80px;width:1200px;height:540px;background:
  radial-gradient(ellipse 1400px 260px at 50% 118%, #9fb9d8 0%, #46648f 30%, #142440 55%, transparent 72%),
  linear-gradient(#07090f,#0d1426 60%,#1a2a48)}
.hero-frame{left:392px;top:160px;width:416px;height:340px;border:2px solid rgba(255,255,255,.9);text-align:center;color:#fff}
.hero-title{margin-top:40px;font-size:40px;font-weight:300;line-height:1.3}
.hero-sub{margin-top:12px;font-family:"Lato",sans-serif;font-size:17px;color:var(--red)}
.hero-name{margin-top:62px;font-family:"Lato",sans-serif;font-weight:700;font-size:28px;letter-spacing:1px;color:#fff}
.slider-dots{left:570px;top:642px;display:flex;gap:12px}
.slider-dots i{width:9px;height:9px;border-radius:50%;background:#ccc}
.slider-dots i:first-child{background:var(--accent)}

/* section heading */
.section-head{left:0;width:1200px;text-align:center}
.section-head h2{font-family:"Lato",sans-serif;font-weight:300;font-size:36px;letter-spacing:2px;color:var(--ink)}
.section-head p{display:inline-block;margin-top:12px;padding-top:10px;border-top:1px solid var(--ink);font-size:13px;color:var(--muted)}

/* product cards */
.card-media{width:300px;height:176px;border-radius:2px}
.card-text{width:300px;font-size:13px;line-height:1.7;color:var(--muted)}
.more-btn{left:352px;width:496px;height:56px;background:#e6e6e6;border:1px solid #d2d2d2;display:flex;align-items:center;justify-content:center;font-family:"Lato",sans-serif;font-size:15px;letter-spacing:2px;color:#555}
.more-btn .plus{position:absolute;left:24px;font-size:20px;color:#888}

.divider{left:0;top:1236px;width:1200px;height:1px;background:var(--line)}

/* blog cards */
.post-media{width:300px;height:180px}
.post-tag{left:0;top:0;background:var(--accent);color:#fff;font-family:"Lato",sans-serif;font-size:12px;padding:3px 10px}
.post-date{font-family:"Lato",sans-serif;font-size:13px;color:var(--accent-dark)}
.post-text{width:300px;font-size:13px;line-height:1.7;color:var(--muted)}

/* footer */
.to-top{left:584px;top:2128px}
.site-footer{left:0;top:2160px;width:1200px;height:268px;background:var(--footer)}
.footer-brand{left:180px;top:2208px;font-family:"Lato",sans-serif;font-weight:700;font-size:26px;letter-spacing:1px;color:#fff}
.social{left:436px;top:2216px;display:flex;gap:14px}
.social i{width:20px;height:20px;border-radius:50%;background:#ddd}
.footer-copy{left:180px;top:2268px;width:420px;font-size:13px;line-height:1.8;color:var(--footer-text)}
.contact-btn{left:652px;top:2246px;width:368px;height:62px;background:var(--accent);color:#fff;display:flex;align-items:center;justify-content:center;font-family:"Lato",sans-serif;font-size:17px;letter-spacing:2px}
.contact-btn::before{content:"›";position:absolute;left:22px;font-size:22px}
.footer-links{left:652px;top:2330px;font-size:13px;color:var(--footer-text)}
.copyright{left:652px;top:2362px;font-family:"Lato",sans-serif;font-size:12px;color:#888}
</style>
</head>
<body>

<header class="site-header abs">
  <div class="brand abs">Norte Studio</div>
  <nav class="main-nav abs"><a>HOME</a><a>PRODUCTS</a><a>BLOG</a><a>CONTACT</a></nav>
</header>

<section class="hero abs" role="img" aria-label="宇宙から見た夜の地球と星空"></section>
<div class="hero-frame abs">
  <h1 class="hero-title">世界は、<br>もっとデザインできる</h1>
  <p class="hero-sub">The world can be designed more</p>
  <p class="hero-name">Norte Studio</p>
</div>
<div class="slider-dots abs"><i></i><i></i><i></i></div>

<div class="section-head abs" style="top:700px"><h2>PRODUCTS</h2><p>製品紹介</p></div>

<div class="card-media abs" style="left:120px;top:832px;background:linear-gradient(135deg,#3a3530,#1c1c1c 60%,#c9a86b)" role="img" aria-label="木製デスク上のスマートフォンと照明"></div>
<div class="card-media abs" style="left:450px;top:832px;background:linear-gradient(135deg,#7fa6bf,#d8dfe4 60%,#8a9aa6)" role="img" aria-label="ワイヤーでできた作品を持つ手"></div>
<div class="card-media abs" style="left:780px;top:832px;background:linear-gradient(#f4f4f4,#e2e2e2)" role="img" aria-label="ウェブサイトを表示したノートパソコン"></div>
<p class="card-text abs" style="left:120px;top:1024px">新しいアプリの概要がここに入ります。製品の特長を短く紹介します。</p>
<p class="card-text abs" style="left:450px;top:1024px">新しいサービスの概要がここに入ります。製品の特長を短く紹介します。</p>
<p class="card-text abs" style="left:780px;top:1024px">新しいツールの概要がここに入ります。製品の特長を短く紹介します。</p>
<div class="more-btn abs" style="top:1110px"><span class="plus">+</span>MORE</div>

<div class="divider abs"></div>

<div class="section-head abs" style="top:1284px"><h2>BLOG</h2><p>ブログ</p></div>

<div class="post-media abs" style="left:120px;top:1412px;background:linear-gradient(#d9dde2,#9aa3ad)" role="img" aria-label="明るいオフィスの室内"><span class="post-tag abs">Category</span></div>
<div class="post-media abs" style="left:450px;top:1412px;background:linear-gradient(#a9b98a,#5d6b49)" role="img" aria-label="屋外に置かれた自転車"><span class="post-tag abs">Category</span></div>
<div class="post-media abs" style="left:780px;top:1412px;background:linear-gradient(#c8d2d8,#7b8793)" role="img" aria-label="街中に停まる電気自動車"><span class="post-tag abs">Category</span></div>
<span class="post-date abs" style="left:120px;top:1602px">2015.01.01</span>
<span class="post-date abs" style="left:450px;top:1602px">2015.01.01</span>
<span class="post-date abs" style="left:780px;top:1602px">2015.01.01</span>
<p class="post-text abs" style="left:120px;top:1626px">記事の要約がここに入ります。技術情報を短くまとめて紹介します。</p>
<p class="post-text abs" style="left:450px;top:1626px">記事の要約がここに入ります。技術情報を短くまとめて紹介します。</p>
<p class="post-text abs" style="left:780px;top:1626px">記事の要約がここに入ります。技術情報を短くまとめて紹介します。</p>

<div class="post-media abs" style="left:120px;top:1700px;background:linear-gradient(#f0b45a,#c7782a)" role="img" aria-label="飛行するドローン"><span class="post-tag abs">Category</span></div>
<div class="post-media abs" style="left:450px;top:1700px;background:linear-gradient(#8c8f94,#3f4247)" role="img" aria-label="スーツ姿の登壇者"><span class="post-tag abs">Category</span></div>
<div class="post-media abs" style="left:780px;top:1700px;background:linear-gradient(#e9d6c3,#b99a7d)" role="img" aria-label="食事をする子ども"><span class="post-tag abs">Category</span></div>
<span class="post-date abs" style="left:120px;top:1890px">2015.01.01</span>
<span class="post-date abs" style="left:450px;top:1890px">2015.01.01</span>
<span class="post-date abs" style="left:780px;top:1890px">2015.01.01</span>
<p class="post-text abs" style="left:120px;top:1914px">記事の要約がここに入ります。技術情報を短くまとめて紹介します。</p>
<p class="post-text abs" style="left:450px;top:1914px">記事の要約がここに入ります。技術情報を短くまとめて紹介します。</p>
<p class="post-text abs" style="left:780px;top:1914px">記事の要約がここに入ります。技術情報を短くまとめて紹介します。</p>
<div class="more-btn abs" style="top:1998px"><span class="plus">+</span>MORE</div>

<svg class="to-top abs" width="32" height="20" viewBox="0 0 32 20" aria-hidden="true"><polyline points="6,14 16,6 26,14" fill="none" stroke="#999" stroke-width="2"/></svg>

<footer class="site-footer abs"></footer>
<div class="footer-brand abs">Norte Studio</div>
<div class="social abs"><i></i><i></i><i></i></div>
<p class="footer-copy abs">私たちはアプリやサービスの開発を通じて、蓄積した技術情報を発信しています。新しい体験をデザインし、より良い世界づくりに貢献します。</p>
<div class="contact-btn abs">CONTACT</div>
<p class="footer-links abs">› 運営会社</p>
<p class="copyright abs">All Rights Reserved. Copyright 2015 Norte Studio</p>

</body>
</html>
```